IT services company needs a business card designed

-2 sided business card.-Front is going to be the logo raised (3D floating effect) on a black background. Make the logos spider web shiny silver and keep the spider the same design. -Back needs to have the following information:Doug Farrow, Managing Partner, Cell: 602-488-3179, Website: Kolvantra.com, Email: Doug@Kolvantra.com
Target Market(s)
IT Services
Industry/Entity Type
It Company
Contact Information for Business Card
-2 sided business card.
-Front is going to be the logo raised (3D floating effect) on a black background. Make the logos spider web shiny silver and keep the spider the same design.
-Back needs to have the following information:
Doug Farrow, Managing Partner, Cell: 602-488-3179, Website: Kolvantra.com, Email: Doug@Kolvantra.com
Look and feel

```html
<!DOCTYPE html>
<html lang="en">
<head>
<meta charset="utf-8">
<title>Kolvantra Business Card</title>
<link href="https://fonts.googleapis.com/css2?family=Exo+2:wght@400;500&display=swap" rel="stylesheet">
<style>
  :root {
    --backdrop: #4a4a4a;
    --card: #1c1c1e;
    --card-edge: #2a2a2c;
    --silver: #cfd2d6;
    --text-grey: #c4c6c9;
    --accent: #1aa3e0;
    --accent-deep: #0d6fae;
    --stripe-line: #9a9ea3;
  }
  * { margin: 0; padding: 0; box-sizing: border-box; }
  html, body {
    width: 1200px; height: 1000px; overflow: hidden;
    background: var(--backdrop);
    font-family: "Exo 2", sans-serif;
  }
  .card {
    position: absolute;
    width: 640px; height: 366px;
    left: 280px;
    background: linear-gradient(160deg, var(--card-edge), var(--card) 60%);
    border-radius: 22px;
    overflow: hidden;
  }
  .card-front { top: 60px; }
  .card-back { top: 540px; }

  .front-mark {
    position: absolute; inset: 0;
    display: flex; flex-direction: column; align-items: center; justify-content: center;
    gap: 24px;
  }
  .front-mark .dot {
    width: 120px; height: 120px; border-radius: 50%;
    background: var(--silver);
  }
  .front-mark .brand-name {
    font-size: 62px; font-weight: 400; letter-spacing: 2px;
    color: var(--silver); text-transform: uppercase;
  }

  .back-stripe {
    position: absolute; left: 0; top: 0; bottom: 0; width: 36px;
    background: var(--accent);
    border-right: 7px solid var(--stripe-line);
  }
  .back-brand {
    position: absolute; left: 70px; top: 90px; z-index: 2;
    font-size: 40px; font-weight: 400; letter-spacing: 1px;
    color: var(--silver); text-transform: uppercase;
  }
  .contact-block { position: absolute; left: 70px; top: 170px; z-index: 2; }
  .person { display: flex; align-items: baseline; gap: 14px; margin-bottom: 12px; white-space: nowrap; }
  .person-name { font-size: 26px; color: var(--accent); text-transform: uppercase; letter-spacing: 1px; }
  .person-role { font-size: 17px; color: var(--text-grey); }
  .contact-line {
    display: flex; align-items: center; gap: 10px;
    font-size: 18px; color: var(--text-grey); margin-bottom: 6px;
  }
  .contact-line svg { width: 16px; height: 16px; flex: none; }
  .contact-line .hl { color: var(--accent); }

  .spider-art {
    position: absolute; right: 0; bottom: 0; width: 196px; height: 290px; z-index: 1;
    background: radial-gradient(circle at 62% 55%, var(--accent) 0%, var(--accent-deep) 35%, #3b3d40 70%, var(--card) 100%);
    border-top-left-radius: 110px;
  }
</style>
</head>
<body>
  <section class="card card-front">
    <div class="front-mark">
      <div class="dot"></div>
      <div class="brand-name">Kolvantra</div>
    </div>
  </section>

  <section class="card card-back">
    <div class="back-stripe"></div>
    <div class="back-brand">Kolvantra</div>
    <div class="contact-block">
      <div class="person">
        <span class="person-name">Doug Farrow</span>
        <span class="person-role">Managing Partner</span>
      </div>
      <div class="contact-line">
        <svg viewBox="0 0 16 16"><path d="M3 1l3 3-1.5 2a9 9 0 0 0 5.5 5.5L12 10l3 3-2 2C7 15 1 9 1 3z" fill="#c4c6c9"/></svg>
        602-488-3179
      </div>
      <div class="contact-line">
        <svg viewBox="0 0 16 16"><rect x="1" y="3" width="14" height="10" rx="1" fill="none" stroke="#c4c6c9" stroke-width="1.5"/><path d="M1 4l7 5 7-5" fill="none" stroke="#c4c6c9" stroke-width="1.5"/></svg>
        Doug@Kolvantra.com
      </div>
      <div class="contact-line">
        <svg viewBox="0 0 16 16"><circle cx="8" cy="8" r="6.5" fill="none" stroke="#c4c6c9" stroke-width="1.4"/><ellipse cx="8" cy="8" rx="3" ry="6.5" fill="none" stroke="#c4c6c9" stroke-width="1.2"/><path d="M1.5 8h13" stroke="#c4c6c9" stroke-width="1.2"/></svg>
        <span>www.<span class="hl">Kolvantra</span>.com</span>
      </div>
    </div>
    <div class="spider-art" role="img" aria-label="Blue low-poly spider on a silver and blue circuit web"></div>
  </section>
</body>
</html>
```